Coralvale Jukebox and Jumping Castle Hire

Hi folks,
This is for a new business based in Brisbane(Australia), the business hires, jukeboxes, inflatable games(mostly jumping castles) and slushy/cocktail machines.
I want the website to appeal to people looking to party. Does that sound too simplistic?
It should be simple to navigate, I require only the front page but make it easy to get to the rest of the site.
Modern, exciting and funky, think rock band or concert promoter.
We are trying to sell packages of products, there should be several packages visible on the front page without looking cluttered.
Link to jukebox song list.
Friendlane, pondlet etc.
I am currently on holidays so I have a fair amount of time to get this project done, it says 10 days I hope to have it done much sooner.

Reason: So far there is no design that I am happy with. I am after a website for Jukeboxes, it should have a rock concert feel.

Ages 20 to 50

Business

• Think rock band type website, black with bold color highlight.
• Plain or bland color.
Pictures of Brisbane or any other city.
Vexaro map or any other location type map.

```html
<!DOCTYPE html>
<html lang="en">
<head>
<meta charset="utf-8">
<title>Coralvale Jukebox and Jumping Castle Hire</title>
<link href="https://fonts.googleapis.com/css2?family=Open+Sans:wght@400;600;700&family=PT+Serif&display=swap" rel="stylesheet">
<style>
:root{
  --black:#000;
  --panel:#0b0b0b;
  --orange:#ff9e00;
  --orange-deep:#f08a00;
  --orange-light:#ffb21c;
  --white:#fff;
  --grey:#cfcfcf;
  --field:#d9d9d9;
  --line:#8a8a8a;
}
*{margin:0;padding:0;box-sizing:border-box}
html,body{width:820px;height:1200px;overflow:hidden;background:var(--black)}
body{position:relative;font-family:"Open Sans",sans-serif;color:var(--white)}
.abs{position:absolute}

.hero{left:0;top:0;width:820px;height:423px;
  background:radial-gradient(ellipse at 68% 55%,#ff9a1a 0%,#d2400f 22%,#5a1a0c 45%,#1e1510 70%,#0d0c0a 100%)}
.brand{left:88px;top:0;width:118px;height:130px;background:rgba(0,0,0,.88);text-align:center;padding-top:58px}
.brand-mark{width:22px;height:22px;border-radius:50%;background:var(--orange);margin:0 auto 6px}
.brand-name{font-size:19px;font-weight:600;letter-spacing:.5px;line-height:1}
.brand-tag{font-size:6px;margin-top:3px}
.social-top{right:89px;top:15px;display:flex;gap:3px}
.social-top span{width:11px;height:11px;border-radius:50%;background:#6b6b6b}
.nav{left:260px;top:42px;width:471px;height:35px;background:rgba(0,0,0,.85);border-radius:2px}
.nav ul{list-style:none;display:flex;position:absolute;left:32px;top:10px;gap:0}
.nav a{color:var(--white);text-decoration:none;font-size:10px;font-weight:600;padding:3px 11px;display:block;border-radius:2px}
.nav a.active{background:var(--orange);color:#222;font-weight:400}
.nav li+li a{margin-left:6px}
.search{left:337px;top:10px;width:126px;height:17px;background:#eee;border:0;border-radius:2px;font-size:9px;font-style:italic;color:#aaa;padding-left:12px;line-height:17px}
.slide-title{left:90px;top:130px;width:198px;height:63px;background:rgba(0,0,0,.5);color:var(--orange);font-size:45px;line-height:60px;padding-left:6px}
.arrow{top:220px;width:32px;height:32px;border-radius:50%;background:rgba(0,0,0,.55)}
.dots{left:305px;top:391px;display:flex;gap:8px}
.dots span{width:65px;height:8px;border-radius:4px;background:rgba(0,0,0,.65)}
.dots span.on{background:var(--orange)}

.welcome{left:0;top:423px;width:820px;height:94px;background:linear-gradient(#ffa800,var(--orange-deep));color:#111;text-align:center}
.welcome h1{font-size:19px;font-weight:700;margin-top:23px;line-height:24px}
.welcome h2{font-size:28px;font-weight:400;line-height:32px}

.intro{left:110px;top:537px;width:600px;font-size:8.2px;line-height:11px;text-align:center}
.btn{background:linear-gradient(var(--orange-light),var(--orange-deep));color:#111;font-family:"PT Serif",serif;font-size:6.5px;text-transform:uppercase;border:1px solid #5a3300;text-align:center;line-height:17px}
.intro-btn{left:386px;top:572px;width:48px;height:19px}

.photo{background:linear-gradient(135deg,#1b2a66,#7a3590 55%,#211a2a)}
.tile{width:212px;height:155px}
.tile h3{font-size:14px;font-weight:400;color:var(--orange);letter-spacing:.3px;margin:18px 0 8px}
.tile p{font-size:8.6px;line-height:11.3px;color:var(--white)}
.tile .btn{position:absolute;width:48px;height:19px}

.footer-rule{left:0;top:958px;width:820px;height:3px;background:var(--orange)}
.tab{left:397px;top:945px}
.f-head{font-size:12.5px;color:var(--orange);font-weight:400;top:972px}
.circles{left:88px;top:997px;display:flex;gap:9px}
.circles span{width:24px;height:24px;border-radius:50%;background:#555}
.circles span:first-child{background:var(--orange)}
.blogs{left:88px;top:1047px;width:180px}
.blogs h4{font-size:12px;font-weight:400;margin-bottom:10px}
.blogs h5{font-size:8.8px;font-weight:400}
.blogs time{display:block;font-size:5.5px;color:var(--orange);margin:4px 0 3px}
.blogs p{font-size:8px;line-height:12px}
.blogs a{display:block;font-family:"PT Serif",serif;font-size:7.5px;color:var(--orange);text-decoration:none;margin-top:10px}
.ads{left:308px;top:995px;width:179px;list-style:none}
.ads li{font-size:7px;height:16.5px;line-height:16px;border-bottom:1px solid var(--line);padding-left:8px;position:relative}
.ads li::before{content:"»";position:absolute;left:0;color:var(--grey)}
.field{background:var(--field);color:#777;font-family:"PT Serif",serif;font-size:8px;padding:3px 6px;border:0;position:absolute;left:551px;width:181px}
.submit{left:684px;top:1139px;width:48px;height:20px;font-size:7.5px}
.bottom{left:0;top:1181px;width:820px;height:19px;background:linear-gradient(var(--orange-light),var(--orange-deep))}
</style>
</head>
<body>

<header>
  <div class="abs hero" role="img" aria-label="Photo of a glowing orange and red jukebox in a bar"></div>
  <div class="abs brand">
    <div class="brand-mark"></div>
    <div class="brand-name">CORALVALE</div>
    <div class="brand-tag">Jukebox and Jumping Castle Hire</div>
  </div>
  <div class="abs social-top" aria-label="Social links">
    <span title="Linkora"></span><span title="Friendlane"></span><span title="Vexaro"></span><span title="pondlet"></span><span title="Streamly"></span>
  </div>
  <nav class="abs nav">
    <ul>
      <li><a class="active" href="#">Home</a></li>
      <li><a href="#">About</a></li>
      <li><a href="#">FAQ</a></li>
      <li><a href="#">Order</a></li>
      <li><a href="#">Contact</a></li>
    </ul>
    <div class="abs search">Search</div>
  </nav>
  <div class="abs slide-title">Jukebox</div>
  <svg class="abs arrow" style="left:54px" viewBox="0 0 32 32"><path d="M19 9l-7 7 7 7" stroke="#fff" stroke-width="3" fill="none"/></svg>
  <svg class="abs arrow" style="left:737px" viewBox="0 0 32 32"><path d="M13 9l7 7-7 7" stroke="#222" stroke-width="3" fill="none"/></svg>
  <div class="abs dots"><span></span><span class="on"></span><span></span></div>
</header>

<section class="abs welcome">
  <h1>Welcome To Coralvale</h1>
  <h2>Jukebox &amp; Jumping Castle Hire</h2>
</section>

<main>
  <p class="abs intro">Contrary to popular belief, Lorem Ipsum is not simply random text. It has roots in a piece of classical Latin literature from 45 BC, making it over 2000 years old. Edwin Marlowe, a Latin professor at Ashgrove-Lindell College in Carolina, looked up one of the more obscure Latin words, consectetur</p>
  <div class="abs btn intro-btn">Learn more</div>

  <div class="abs tile photo" style="left:88px;top:617px;width:217px" role="img" aria-label="Photo of a man beside a touchscreen jukebox"></div>
  <div class="abs tile" style="left:305px;top:617px;padding:0 15px">
    <h3>INFLATABLE GAMES</h3>
    <p>Phasellus porta. Fusce suscipit varius mi. Cum sociis natoque penatibus et magnis dis parturient montes, Phasellus porta. Fusce suscipit varius mi. Cum sociis natoque penatibus et magnis dis parturient montes,</p>
    <div class="btn" style="left:147px;top:116px">Learn more</div>
  </div>
  <div class="abs tile" style="left:517px;top:617px;width:217px;background:linear-gradient(120deg,#1a1010,#e03070 35%,#8fd020 60%,#9a30c0 85%,#150a15)" role="img" aria-label="Photo of hands holding colourful slushy cocktails"></div>

  <div class="abs tile" style="left:88px;top:772px;width:217px;padding:0 10px">
    <h3>JUKEBOXES</h3>
    <p>Phasellus porta. Fusce suscipit varius mi. Cum sociis natoque penatibus et magnis dis parturient montes, Phasellus porta. Fusce suscipit varius mi. Cum sociis natoque penatibus et magnis dis parturient montes,</p>
    <div class="btn" style="left:159px;top:131px">Learn more</div>
  </div>
  <div class="abs tile" style="left:305px;top:772px;background:linear-gradient(#2fa040,#2b3fb8 35%,#e23a2a 70%,#f1d32a)" role="img" aria-label="Photo of a colourful inflatable boxing ring"></div>
  <div class="abs tile" style="left:517px;top:772px;width:217px;padding:0 13px">
    <h3>SLUSHY / COCKTAIL</h3>
    <p>Phasellus porta. Fusce suscipit varius mi. Cum sociis natoque penatibus et magnis dis parturient montes, Phasellus porta. Fusce suscipit varius mi. Cum sociis natoque penatibus et magnis dis parturient montes,</p>
    <div class="btn" style="left:168px;top:131px">Learn more</div>
  </div>
</main>

<footer>
  <svg class="abs tab" width="28" height="14" viewBox="0 0 28 14"><path d="M0 14L7 0h14l7 14z" fill="#ff9e00"/><rect x="11" y="7" width="6" height="2" fill="#111"/></svg>
  <div class="abs footer-rule"></div>

  <h3 class="abs f-head" style="left:88px">SOCIAL LINKS</h3>
  <div class="abs circles"><span title="Friendlane"></span><span title="pondlet"></span><span title="Linkora"></span></div>
  <div class="abs blogs">
    <h4>BLOGS</h4>
    <h5>Post Title</h5>
    <time>Friday, 6th April 2000</time>
    <p>Lorem ipsum dolor sit amet, consectetur adipiscing elit. Nunc non diam erat. In fringilla massa ut nisi ullamcorper pellentesque.</p>
    <a href="#">Read More »</a>
  </div>

  <h3 class="abs f-head" style="left:308px">ADVERTISE WITH US</h3>
  <ul class="abs ads">
    <li>Lorem Ipsum dolor sit</li>
    <li>Amet consectetur</li>
    <li>Praesent vel sem id</li>
    <li>Curabitur hendrerit est</li>
    <li>Aliquam eget erat nec sapien</li>
    <li>Cras id augue nunc</li>
    <li>In nec justo non</li>
    <li>Vivamus mollis enim ut</li>
    <li>Curabitur hendrerit est</li>
  </ul>

  <h3 class="abs f-head" style="left:551px">CONTACT US</h3>
  <div class="field" style="top:996px;height:20px">Name</div>
  <div class="field" style="top:1021px;height:20px">Email</div>
  <div class="field" style="top:1046px;height:75px">Massages</div>
  <div class="abs btn submit">SUBMIT</div>

  <div class="abs bottom"></div>
</footer>

</body>
</html>
```